Business Card Design Project

We need a business card design for a new company based in Singapore called 'Bright Ladder Pte Ltd'. We provide personal development training and emotional intelligence workshops. Our slogan is "Climb beyond your limits". We will not have a company address on the business card. Only phone number, email address and website address.

Target Market(s)

Adults age 25 to 45 years old.
Mostly working in a job.

Industry/Entity Type

Training

Colors
0255a2
f37123

```html
<!DOCTYPE html>
<html lang="en">
<head>
<meta charset="utf-8">
<title>Bright Ladder Pte Ltd – Business Card</title>
<link href="https://fonts.googleapis.com/css2?family=Roboto:wght@300;400;500&display=swap" rel="stylesheet">
<style>
  :root {
    --navy: #1e3c6a;
    --navy-deep: #1c3866;
    --navy-light: #587a9c;
    --orange: #ef6a2a;
    --orange-light: #f2874f;
    --paper: #ffffff;
    --backdrop: #ececec;
    --ink: #1e3c6a;
  }
  * { margin: 0; padding: 0; box-sizing: border-box; }
  html, body {
    width: 1200px; height: 720px; overflow: hidden;
    background: var(--backdrop);
    font-family: "Roboto", Arial, sans-serif;
  }
  .stage { position: relative; width: 1200px; height: 720px; }
  .card { position: absolute; top: 240px; width: 420px; height: 240px; overflow: hidden; }
  .card-front {
    left: 147px;
    background: linear-gradient(20deg, var(--navy-deep) 20%, var(--navy-light) 100%);
  }
  .card-back { left: 633px; background: var(--paper); }

  /* brand lockup */
  .brand-dot { position: absolute; border-radius: 50%; }
  .brand-name { position: absolute; display: flex; flex-direction: column; align-items: flex-end; }
  .brand-title { font-weight: 500; line-height: 1; white-space: nowrap; }
  .brand-suffix {
    display: flex; align-items: center; width: 100%;
    font-weight: 300; text-transform: uppercase; letter-spacing: 0.12em; line-height: 1;
  }
  .brand-suffix::before { content: ""; flex: 1; height: 1px; margin-right: 6px; background: currentColor; }

  .card-front .brand-dot { left: 84px; top: 78px; width: 66px; height: 66px; background: #fff; }
  .card-front .brand-name { left: 156px; top: 89px; color: #fff; }
  .card-front .brand-title { font-size: 30px; }
  .card-front .brand-suffix { font-size: 14px; margin-top: 4px; }

  .tagline-band {
    position: absolute; left: 0; top: 195px; width: 100%; height: 24px;
    background: linear-gradient(90deg, var(--orange), var(--orange-light));
    display: flex; align-items: center; justify-content: center;
    color: #fff; font-weight: 300; font-size: 13px;
    letter-spacing: 0.3em; word-spacing: 0.35em; text-transform: uppercase;
  }

  .card-back .brand-dot { left: 18px; top: 95px; width: 44px; height: 44px; background: var(--navy); }
  .card-back .brand-name { left: 69px; top: 101px; color: var(--navy); }
  .card-back .brand-title { font-size: 20px; }
  .card-back .brand-suffix { font-size: 10.5px; margin-top: 3px; }

  .divider { position: absolute; left: 210px; top: 87px; width: 1px; height: 60px; background: var(--navy); }
  .contact-list {
    position: absolute; left: 224px; top: 92px; list-style: none;
    font-size: 12px; line-height: 17.6px; color: var(--ink);
  }
  .contact-list .label { font-weight: 500; }
  .contact-list .value { color: var(--orange); }

  .stripe-orange { position: absolute; left: 0; top: 198px; width: 100%; height: 5px; background: var(--orange); }
  .band-navy {
    position: absolute; left: 0; top: 206px; width: 100%; height: 34px;
    background: linear-gradient(90deg, var(--navy), #26467a);
  }
</style>
</head>
<body>
<main class="stage">
  <section class="card card-front" aria-label="Business card front">
    <span class="brand-dot"></span>
    <div class="brand-name">
      <span class="brand-title">Bright Ladder</span>
      <span class="brand-suffix">Pte Ltd</span>
    </div>
    <div class="tagline-band">Climb beyond your limits</div>
  </section>

  <section class="card card-back" aria-label="Business card back">
    <span class="brand-dot"></span>
    <div class="brand-name">
      <span class="brand-title">Bright Ladder</span>
      <span class="brand-suffix">Pte Ltd</span>
    </div>
    <div class="divider"></div>
    <ul class="contact-list">
      <li><span class="label">Phone:</span> <span class="value">+ 65 6210 4837</span></li>
      <li><span class="label">Email:</span> <span class="value">hello@brightladder.com</span></li>
      <li><span class="label">Website:</span> <span class="value">www.brightladder.com</span></li>
    </ul>
    <div class="stripe-orange"></div>
    <div class="band-navy"></div>
  </section>
</main>
</body>
</html>
```